world's hottest chilli salt 7 flavours

I am needing a packaging design for 7 different ones to reflect our range

We are located in Perth OZ. Our chilli salts are new and unique and the world’s hottest ones as we use the world’s hottest chillies. Our product is made from chilli and salts but then other flavours to make them different - one for example is a Smokey one which is very popular and it made from salt, chilli, chipotle, coriander, yellow mustard seeds and garlic.

the colour distinguishes the difference between the different flavours

ingredient list is on the website for each flavour
please view fernmoltaskel.com at our range of chilli salts

Target Market(s)

Male adults age is from 18 + - target market is Australian market but will be selling overseas as well to the US.

Industry/Entity Type

Product

Requirements
Must have
• must be colour code as examples i have uploaded whether or to view fernmoltaskels.com -it it bigger or small i'm not fussed but there needs to be a distinction between the 7 different flavours. Size of label is 95mm x 37mm to work from so very small. The relish the blaze (attached) needs to be somewhere on the logo but i would like to see what someone can do with that.
the logo is found with the tongue attached - this is needed and to be quite big if possible – we need the chilli image. It needs to be a good design where our customers and us go WOW.

text of the salts is found on the website.

barcode is needed along the right side. but do not include in the image i will put that on myself

also ingredient list - this is currently not looking any good.

needs to be the "worlds hottest" somewhere
Nice to have
• something clean crisp and elegant like

http://crateloomviews.examplehost.net/2009/10/plain-drop.html

** this is what we would like http://3.img.examplehost.net/_9QwLrTzXpaM/RkPd-7NnvGs/AAAAAAAAH2K/kTr4WZxeLPQ/s1600/KLMV+cards.jpg
clean crisp and
Should not have
• too many fonts

```html
<!DOCTYPE html>
<html lang="en">
<head>
<meta charset="utf-8">
<title>Kestrel Pantry – World's Hottest Chilli Salt Label</title>
<link href="https://fonts.googleapis.com/css2?family=Archivo:wght@800&family=Arimo:wght@400;700&display=swap" rel="stylesheet">
<style>
  :root {
    --page: #ffffff;
    --label-dark: #231f20;
    --label-ghost: #3a3839;
    --chilli-red: #ed1c24;
    --heading-red: #e8242b;
    --text-light: #ffffff;
    --logo-flame: #f7c21a;
    --logo-pepper: #c81e25;
  }
  * { margin: 0; padding: 0; box-sizing: border-box; }
  html, body {
    width: 1200px; height: 900px; overflow: hidden;
    background: var(--page);
    font-family: "Arimo", Arial, sans-serif;
  }
  .label {
    position: absolute; left: 26px; top: 225px;
    width: 1122px; height: 437px;
    background: var(--label-dark);
    overflow: hidden;
    color: var(--text-light);
  }
  .ghost-word {
    position: absolute;
    font-family: "Archivo", "Arimo", Arial, sans-serif;
    font-weight: 800; font-size: 330px; line-height: 330px;
    color: var(--label-ghost);
    letter-spacing: -8px;
    white-space: nowrap;
  }
  .ghost-chilli { left: 84px; top: -120px; }
  .ghost-spice { left: 166px; top: 178px; }
  .hottest-band {
    position: absolute; left: 0; top: 0;
    width: 84px; height: 100%;
    background: var(--chilli-red);
    display: flex; align-items: center; justify-content: center;
  }
  .hottest-band span {
    transform: rotate(-90deg);
    white-space: nowrap;
    font-weight: 700; font-size: 40px;
    color: var(--text-light);
  }
  .product-name {
    position: absolute; left: 126px; top: 78px;
    font-weight: 700; font-size: 41px; line-height: 45px;
    color: var(--heading-red);
    white-space: nowrap;
  }
  .product-blurb {
    position: absolute; left: 129px; top: 236px;
    font-size: 20px; line-height: 24px;
    color: var(--text-light);
    white-space: nowrap;
  }
  .heat-row {
    position: absolute; left: 130px; top: 348px;
    display: flex; align-items: center; height: 56px;
  }
  .heat-icons { display: flex; margin-right: 10px; }
  .heat-level { font-size: 27px; }
  .divider {
    width: 2px; height: 54px; background: var(--text-light);
    margin: 0 16px 0 20px;
  }
  .site { font-weight: 700; font-size: 27px; }
  .brand-mark {
    position: absolute; left: 944px; top: 22px;
    width: 160px; display: flex; flex-direction: column; align-items: center;
  }
  .brand-mascot {
    width: 120px; height: 180px; border-radius: 60px 60px 44px 44px;
    background: linear-gradient(160deg, var(--logo-flame) 0%, var(--logo-pepper) 45%, #8e1217 100%);
  }
  .brand-name {
    margin-top: 12px;
    font-weight: 700; font-size: 19px; line-height: 22px;
    color: var(--text-light);
    text-align: center;
  }
  .maker-info {
    position: absolute; left: 962px; top: 288px;
    font-size: 16px; line-height: 17px;
  }
  .maker-info .origin { color: var(--heading-red); font-weight: 700; }
  .net-weight {
    position: absolute; left: 961px; top: 364px;
    font-weight: 700; font-size: 25px; color: var(--heading-red);
  }
</style>
</head>
<body>
  <div class="label">
    <div class="ghost-word ghost-chilli" aria-hidden="true">CHILLI</div>
    <div class="ghost-word ghost-spice" aria-hidden="true">SPICE</div>

    <div class="hottest-band"><span>WORLD’S HOTTEST</span></div>

    <h1 class="product-name">Bhut Jolokia Chilli<br>(World’s Hottest Chilli)<br>&amp; Pink Himilayan Rock Salt</h1>

    <p class="product-blurb">An excellent all-round salt to enhance the flavour<br>of any meal. Adds a little salt and lots of zing! No MSG.</p>

    <div class="heat-row">
      <div class="heat-icons" aria-hidden="true">
        <svg width="104" height="56" viewBox="0 0 104 56">
          <g fill="#ed1c24">
            <path d="M6 16 C0 26 4 42 18 52 C24 56 32 52 28 46 C20 38 16 28 18 18 C18 10 10 8 6 16Z"/>
            <path d="M12 12 C12 6 16 2 20 4 C17 6 16 9 17 13 Z"/>
            <path d="M40 16 C34 26 38 42 52 52 C58 56 66 52 62 46 C54 38 50 28 52 18 C52 10 44 8 40 16Z"/>
            <path d="M46 12 C46 6 50 2 54 4 C51 6 50 9 51 13 Z"/>
            <path d="M74 16 C68 26 72 42 86 52 C92 56 100 52 96 46 C88 38 84 28 86 18 C86 10 78 8 74 16Z"/>
            <path d="M80 12 C80 6 84 2 88 4 C85 6 84 9 85 13 Z"/>
          </g>
        </svg>
      </div>
      <span class="heat-level">VERY HOT</span>
      <span class="divider"></span>
      <span class="site">fernmoltaskels.com</span>
    </div>

    <div class="brand-mark">
      <div class="brand-mascot" role="img" aria-label="Brand mascot illustration: a red chilli character with flames"></div>
      <div class="brand-name">Kestrel Pantry</div>
    </div>

    <div class="maker-info">
      <div class="origin">MADE IN WA</div>
      <div>PO BOX 452</div>
      <div>Marlow Vale 6021</div>
    </div>
    <div class="net-weight">100g</div>
  </div>
</body>
</html>
```